Ocean Exploration and Sonar Technology Education Website

I need a website for a Ocean Exploration and Sonar technology system. Sonar technology is a system used to scan the ocean for shipwrecks and other exploration services. The website is an education resource for people interested in Sonar systems and their history. The website goal is to tell the history of Sonar systems and provide credit to people who have contributed to the field.
DO NOT CONTACT ME PRIVATELY OFF THIS WEBSITE. PRIVATE MESSAGES WILL BE IGNORED.
Please see included document here
Important:
1. Use only royalty free graphics
2. Use only google fonts
3. A clean, linear layout
4. If you can, use a background image of a sea or ocean for the site
PAGES
Home Page
- Include a top graphic saying of a ship or boat in the ocean doing exploration work saying 'welcome aboard'
- Slide show with images
2.Timeline
3. Publications
4. Books & Video
5. Contact Page

```html
<!DOCTYPE html>
<html lang="en">
<head>
<meta charset="utf-8">
<title>Sonar History – Welcome aboard</title>
<link href="https://fonts.googleapis.com/css2?family=Poppins:wght@400;500;600&family=Roboto:wght@400&display=swap" rel="stylesheet">
<style>
  :root{
    --ocean-deep:#1d3a4d;
    --ocean-mid:#2f5369;
    --ocean-light:#4a6f83;
    --white:#ffffff;
    --ink:#111111;
    --text-dark:#222222;
    --text-muted:#8a8a8a;
    --accent:#1a8fd6;
    --card-shadow:rgba(0,0,0,0.08);
  }
  *{margin:0;padding:0;box-sizing:border-box;}
  html,body{width:1013px;height:1200px;overflow:hidden;background:var(--white);}
  body{position:relative;font-family:'Poppins',sans-serif;}

  .hero{position:absolute;left:0;top:0;width:1013px;height:498px;
    background:radial-gradient(ellipse at 55% 60%,var(--ocean-light) 0%,var(--ocean-mid) 45%,var(--ocean-deep) 100%);}
  .logo{position:absolute;left:44px;top:32px;color:var(--white);font-size:28px;font-weight:400;letter-spacing:.5px;}
  .nav{position:absolute;top:42px;left:0;list-style:none;}
  .nav li{position:absolute;color:rgba(255,255,255,.8);font-size:13px;white-space:nowrap;}
  .nav li.active{color:var(--white);font-weight:500;}
  .hero-title{position:absolute;left:84px;top:136px;color:var(--white);font-size:58px;font-weight:600;letter-spacing:-.5px;line-height:1;}
  .hero-text{position:absolute;left:84px;top:219px;width:470px;color:var(--white);font-size:14px;line-height:21px;}
  .explore{position:absolute;left:84px;top:324px;width:159px;height:40px;border:1px solid var(--white);
    color:var(--white);font-family:'Roboto',sans-serif;font-size:11px;display:flex;align-items:center;justify-content:center;gap:10px;}
  .slide-arrow{position:absolute;top:239px;}
  .dots{position:absolute;left:480px;top:464px;display:flex;gap:3px;}
  .dots span{width:8px;height:8px;border:1px solid var(--white);border-radius:50%;}
  .dots span.on{background:var(--white);}

  .section-head{position:absolute;left:120px;top:623px;height:55px;border-left:8px solid var(--accent);padding-left:16px;}
  .section-kicker{font-size:11.5px;color:var(--text-dark);margin-top:2px;}
  .section-title{font-size:38px;font-weight:500;color:var(--ink);line-height:1;margin-top:2px;}

  .card{position:absolute;top:728px;width:259px;height:352px;background:var(--white);box-shadow:0 2px 12px var(--card-shadow);}
  .card-media{height:151px;}
  .card-title{margin:12px 16px 0;font-size:14px;font-weight:400;color:var(--text-dark);line-height:22px;text-transform:uppercase;}
  .card-text{margin:9px 16px 0;font-family:'Roboto',sans-serif;font-size:10.5px;line-height:13.4px;color:var(--text-muted);}
  .card-btn{position:absolute;left:14px;top:305px;width:231px;height:36px;border:1px solid var(--accent);
    color:var(--accent);font-family:'Roboto',sans-serif;font-size:10px;display:flex;align-items:center;justify-content:center;}
</style>
</head>
<body>
  <header class="hero" role="img" aria-label="Photo of an icebreaker research ship sailing across the open ocean">
    <div class="logo">[Your Logo]</div>
    <ul class="nav">
      <li class="active" style="left:540px">Home</li>
      <li style="left:612px">History</li>
      <li style="left:685px">Publications</li>
      <li style="left:792px">Books &amp; Videos</li>
      <li style="left:918px">Contact</li>
    </ul>
    <h1 class="hero-title">Welcome aboard</h1>
    <p class="hero-text">Our goal is to provide a comprehensive history of Sonar systems and their contributors. Join us on a journey of exploration and discovery</p>
    <div class="explore">EXPLORE NOW
      <svg width="16" height="10" viewBox="0 0 16 10"><path d="M0 5H15M10 1L15 5L10 9" stroke="#fff" stroke-width="1.4" fill="none"/></svg>
    </div>
    <svg class="slide-arrow" style="left:34px" width="14" height="22" viewBox="0 0 14 22"><path d="M11 2L3 11L11 20" stroke="rgba(255,255,255,.8)" stroke-width="2.5" fill="none"/></svg>
    <svg class="slide-arrow" style="left:965px" width="14" height="22" viewBox="0 0 14 22"><path d="M3 2L11 11L3 20" stroke="rgba(255,255,255,.8)" stroke-width="2.5" fill="none"/></svg>
    <div class="dots"><span class="on"></span><span></span><span></span><span></span><span></span></div>
  </header>

  <div class="section-head">
    <p class="section-kicker">History of Sonar systems</p>
    <h2 class="section-title">Timeline</h2>
  </div>

  <article class="card" style="left:84px">
    <div class="card-media" role="img" aria-label="Black and white engraving of early sound experiments from boats" style="background:linear-gradient(180deg,#d8d8d8,#555 60%,#333)"></div>
    <h3 class="card-title">Milestone Chronology<br>Up to 1950</h3>
    <p class="card-text">Lorem ipsum dolor sit amet, consectetur adipiscing elit, sed do eiusmod tempor incididunt ut labore et dolore magna.Lorem ipsum dolor sit amet...</p>
    <div class="card-btn">Read more</div>
  </article>
  <article class="card" style="left:357px">
    <div class="card-media" role="img" aria-label="Photo of a yellow sonar towfish on display in a museum" style="background:linear-gradient(135deg,#6a4a3a,#b9a070 50%,#8a6a50)"></div>
    <h3 class="card-title">Milestone Chronology<br>1951 - 1960</h3>
    <p class="card-text">Lorem ipsum dolor sit amet, consectetur adipiscing elit, sed do eiusmod tempor incididunt ut labore et dolore magna.Lorem ipsum dolor sit amet...</p>
    <div class="card-btn">Read more</div>
  </article>
  <article class="card" style="left:630px">
    <div class="card-media" role="img" aria-label="Photo of a patrol aircraft flying above clouds and sea" style="background:linear-gradient(180deg,#c9d6e3,#5a7fa8 55%,#2a4f86)"></div>
    <h3 class="card-title">Milestone Chronology<br>1961 - 1970</h3>
    <p class="card-text">Lorem ipsum dolor sit amet, consectetur adipiscing elit, sed do eiusmod tempor incididunt ut labore et dolore magna.Lorem ipsum dolor sit amet...</p>
    <div class="card-btn">Read more</div>
  </article>
  <article class="card" style="left:903px">
    <div class="card-media" role="img" aria-label="Sonar scan image showing bowsprit, shadow and ship of a wreck" style="background:linear-gradient(135deg,#f3e6ea,#e2c4cc)"></div>
    <h3 class="card-title">Milestone Chronology<br>1971 - 1980</h3>
    <p class="card-text">Lorem ipsum dolor sit amet, consectetur adipiscing elit, sed do eiusmod tempor incididunt ut labore et dolore magna.Lorem ipsum dolor sit amet...</p>
    <div class="card-btn">Read more</div>
  </article>
</body>
</html>
```